professional business card

A Clean looking business card for a money transfer company. Our company is call Velorix= Transfer + Send = Transcend (next level)
to show professionalism as well as some effects to show digital tech.

1 side to have position, name and address
2 side to have company name and show that we provide money exchange and cross-border money transfer

Target Market(s)

Remittance companies and high net worth individuals

Industry/Entity Type

Finance

Contact Information for Business Card

Name, address, email, title, services- money exchange and cross-border remittance

Requirements
Nice to have
• Digital age feel

```html
<!DOCTYPE html>
<html lang="en">
<head>
<meta charset="UTF-8">
<title>Velorix Business Card</title>
<link rel="stylesheet" href="https://fonts.googleapis.com/css2?family=Montserrat:wght@500&family=Open+Sans:wght@400;600&display=swap">
<style>
  :root {
    --page-bg: #e9e6e1;
    --card-bg: #222e3a;
    --card-accent: #2b3f4e;
    --card-accent-soft: rgba(43, 63, 78, 0);
    --brand-teal: #5ab7c6;
    --text-light: #f2f4f5;
    --rule-teal: #4a9fae;
  }
  * { margin: 0; padding: 0; box-sizing: border-box; }
  html, body {
    width: 1200px;
    height: 900px;
    overflow: hidden;
    background: var(--page-bg);
  }
  .canvas {
    position: relative;
    width: 1200px;
    height: 900px;
  }
  .card {
    position: absolute;
    left: 240px;
    width: 720px;
    height: 400px;
    border-radius: 40px;
    background: var(--card-bg);
    box-shadow: 0 14px 30px rgba(0, 0, 0, 0.22);
    overflow: hidden;
  }
  .card--services { top: 40px; }
  .card--contact { top: 470px; }

  .card__backdrop {
    position: absolute;
    right: 0;
    top: 0;
    width: 380px;
    height: 100%;
    background:
      radial-gradient(ellipse 260px 200px at 62% 45%, var(--card-accent) 0%, var(--card-accent) 45%, var(--card-accent-soft) 100%),
      linear-gradient(120deg, var(--card-accent-soft) 0%, rgba(43, 63, 78, 0.55) 60%, var(--card-accent) 100%);
  }

  .brand {
    position: absolute;
    left: 52px;
    top: 66px;
    display: flex;
    align-items: center;
    gap: 18px;
    z-index: 1;
  }
  .brand__mark {
    width: 44px;
    height: 44px;
    border-radius: 50%;
    background: var(--brand-teal);
  }
  .brand__name {
    font-family: "Montserrat", sans-serif;
    font-weight: 500;
    font-size: 54px;
    letter-spacing: 3px;
    color: var(--text-light);
    text-transform: uppercase;
    line-height: 1;
  }

  .card__footer {
    position: absolute;
    left: 0;
    bottom: 34px;
    width: 470px;
    z-index: 1;
  }
  .footer__label {
    padding-left: 76px;
    font-family: "Open Sans", sans-serif;
    font-weight: 600;
    font-size: 20px;
    color: var(--brand-teal);
    text-transform: uppercase;
    letter-spacing: 0.5px;
    margin-bottom: 6px;
  }
  .footer__role {
    color: var(--text-light);
    font-weight: 400;
    text-transform: none;
  }
  .footer__rule {
    height: 2px;
    background: var(--rule-teal);
    margin-bottom: 10px;
  }
  .footer__detail {
    padding-left: 92px;
    display: flex;
    align-items: center;
    gap: 12px;
    font-family: "Open Sans", sans-serif;
    font-size: 21px;
    color: var(--text-light);
    white-space: nowrap;
  }
  .footer__detail--plain { padding-left: 90px; }
  .pin-icon { width: 16px; height: 22px; flex: none; }
</style>
</head>
<body>
<main class="canvas">

  <section class="card card--services" aria-label="Card front: company and services">
    <div class="card__backdrop" role="img" aria-label="Large faint brand decoration in muted slate blue"></div>
    <div class="brand">
      <span class="brand__mark"></span>
      <span class="brand__name">Velorix</span>
    </div>
    <div class="card__footer">
      <p class="footer__label">Our Services</p>
      <div class="footer__rule"></div>
      <p class="footer__detail footer__detail--plain">Money Exchange And Cross-border Remittance</p>
    </div>
  </section>

  <section class="card card--contact" aria-label="Card back: name, position and address">
    <div class="card__backdrop" role="img" aria-label="Large faint brand decoration in muted slate blue"></div>
    <div class="brand">
      <span class="brand__mark"></span>
      <span class="brand__name">Velorix</span>
    </div>
    <div class="card__footer">
      <p class="footer__label">John Smith | <span class="footer__role">Director</span></p>
      <div class="footer__rule"></div>
      <p class="footer__detail">
        <svg class="pin-icon" viewBox="0 0 16 22" aria-hidden="true">
          <path d="M8 0C3.6 0 0 3.5 0 7.9 0 13.6 8 22 8 22s8-8.4 8-14.1C16 3.5 12.4 0 8 0z" fill="#5ab7c6"/>
          <circle cx="8" cy="8" r="3" fill="#222e3a"/>
        </svg>
        00 dummy city, dummy place 0000
      </p>
    </div>
  </section>

</main>
</body>
</html>
```